Bramblecrest IT Solutions Web Design

We are a new business in Perth Australia specializing in supporting Home residential and Small business with their IT requirements
We believe image and presentation is important and having a eye catching, professional, intuitive website is a must.
Although we are still expanding as business the message we would like to convey to users is that they can trust our work.

Services we provide are
Please refer to text file attached

Future services
- Email hosting
- Domain resller
- Cloud services

A wordpress theme i really like is below.
http://www.layoutquarry.example/wordpress-themes/58316.html
Orange colour included is a preference however a colour that goes withg my logo is fine too.

The logo i would like to include is also attached.

I would like the web site design to be built and coded in wordpress and handed over to me so i can continue updating the content, source will be require.

Target Market(s)

Home residential and Small business users

Industry/Entity Type

Residential

Requirements
Must have
• The form to email function in the contact us page.
Nice to have
• Interactive icons

```html
<!DOCTYPE html>
<html lang="en">
<head>
<meta charset="utf-8">
<title>Bramblecrest IT Solutions</title>
<link href="https://fonts.googleapis.com/css2?family=Roboto:wght@400;500;700&display=swap" rel="stylesheet">
<style>
:root{
  --orange:#d0601f;
  --orange-deep:#b9521a;
  --ink:#1c1c1c;
  --body:#555;
  --paper:#f3f3f3;
  --white:#fff;
  --rule:#d8d8d8;
}
*{margin:0;padding:0;box-sizing:border-box}
html,body{width:808px;height:1200px;overflow:hidden}
body{font-family:'Roboto',sans-serif;background:var(--white);position:relative;color:var(--ink)}
.hero{position:absolute;left:0;top:0;width:808px;height:488px;
  background:
   radial-gradient(ellipse 220px 160px at 290px 170px,rgba(214,140,110,.85),rgba(214,140,110,0) 70%),
   radial-gradient(ellipse 380px 200px at 560px 300px,rgba(70,110,140,.8),rgba(70,110,140,0) 70%),
   linear-gradient(135deg,#cfd6da 0%,#8ea3b1 35%,#5c7a90 65%,#9aaab4 100%);}
.brand{position:absolute;left:69px;top:26px;display:flex;align-items:center;gap:8px}
.brand-mark{width:28px;height:28px;background:var(--orange)}
.brand-name{font-size:17px;font-weight:700;color:var(--ink);letter-spacing:.3px}
.nav{position:absolute;right:66px;top:37px;display:flex;gap:0}
.nav a{font-size:10px;font-weight:500;color:var(--ink);text-decoration:none;padding:3px 5px;margin-left:20px}
.nav a.current{background:var(--orange);color:var(--white)}
.hero-title{position:absolute;left:0;width:808px;top:342px;text-align:center;color:var(--white);font-size:26px;line-height:38px;font-weight:400;text-shadow:0 1px 4px rgba(0,0,0,.3)}
.dots{position:absolute;left:382px;top:450px;display:flex;gap:3px}
.dots span{width:10px;height:10px;border-radius:50%;background:var(--white)}
.dots span.hollow{background:transparent;border:1.5px solid var(--white)}
.features{position:absolute;left:0;top:488px;width:808px;height:262px;background:var(--orange);box-shadow:0 3px 4px rgba(0,0,0,.2)}
.feature{position:absolute;top:50px;width:170px;text-align:center;color:var(--white)}
.feature+.feature{border-left:1px solid rgba(255,255,255,.12)}
.f-icon{width:36px;height:36px;border-radius:50%;background:var(--white);margin:0 auto;display:flex;align-items:center;justify-content:center}
.f-title{font-size:12px;font-weight:700;margin-top:18px}
.f-text{font-size:9px;line-height:17px;margin-top:8px;padding:0 6px}
.btn-line{display:inline-block;font-size:8.5px;font-weight:700;border:1.5px solid rgba(255,255,255,.8);padding:7px 8px;margin-top:20px;color:var(--white)}
.services{position:absolute;left:0;top:750px;width:808px;height:298px;background:var(--paper)}
.s-heading{position:absolute;top:30px;left:0;width:808px;text-align:center;color:var(--orange);font-size:12px;font-weight:700}
.s-rule{position:absolute;top:58px;left:384px;width:40px;height:3px;background:#aaa}
.s-divider{position:absolute;left:403px;top:96px;width:1px;height:170px;background:var(--rule)}
.service{position:absolute;top:106px;width:240px}
.s-icon{position:absolute;top:6px;width:36px;height:36px;border-radius:50%;border:1.5px solid #ccc;background:var(--white);display:flex;align-items:center;justify-content:center}
.s-title{font-size:12.5px;font-weight:700;color:var(--orange)}
.s-text{font-size:9.5px;line-height:18px;color:var(--body);margin-top:10px}
.btn-grey{display:inline-block;font-size:8.5px;font-weight:700;color:var(--orange);border:1.5px solid #ccc;padding:8px 10px;margin-top:19px}
.footer{position:absolute;left:0;top:1048px;width:808px;height:152px;background:var(--white)}
.ft-label{position:absolute;top:27px;font-size:9.5px;font-weight:700}
.ft-contact{position:absolute;left:69px;top:52px;font-size:9.5px}
.social{position:absolute;right:67px;top:47px;display:flex;gap:7px}
.social span{width:21px;height:21px;border-radius:50%;border:1px solid #bbb}
.social span.active{border-color:var(--orange)}
.ft-rule{position:absolute;left:69px;top:95px;width:670px;height:1px;background:var(--rule)}
.ft-links{position:absolute;left:70px;top:116px;font-size:8px}
.ft-links span{margin:0 7px}
.copyright{position:absolute;right:69px;top:116px;font-size:8px}
</style>
</head>
<body>
<header class="hero" role="img" aria-label="Photo of a hand typing on a laptop keyboard">
  <div class="brand"><div class="brand-mark"></div><div class="brand-name">Bramblecrest IT Solutions</div></div>
  <nav class="nav"><a class="current">HOME</a><a>ABOUT US</a><a>SERVICES</a><a>BLOG</a><a>CONTACT US</a></nav>
  <h1 class="hero-title">We are supporting Home residential<br>and Small business</h1>
  <div class="dots"><span></span><span class="hollow"></span><span></span><span></span></div>
</header>

<section class="features">
  <div class="feature" style="left:54px">
    <div class="f-icon"><svg width="16" height="16" viewBox="0 0 16 16"><circle cx="8" cy="8" r="5" fill="none" stroke="#d0601f" stroke-width="3" stroke-dasharray="2.4 1.5"/><circle cx="8" cy="8" r="4" fill="#d0601f"/><circle cx="8" cy="8" r="1.6" fill="#fff"/></svg></div>
    <div class="f-title">Technical Support</div>
    <p class="f-text">Lorem Ipsum is simply dummy text of the printing and typesetting industry. Lorem Ipsum .</p>
    <span class="btn-line">READ MORE</span>
  </div>
  <div class="feature" style="left:232px">
    <div class="f-icon"><svg width="16" height="16" viewBox="0 0 16 16" fill="#d0601f"><rect x="6" y="1" width="4" height="4"/><rect x="1" y="11" width="4" height="4"/><rect x="6" y="11" width="4" height="4"/><rect x="11" y="11" width="4" height="4"/><path d="M7.5 5v3M3 11V8h10v3M8 8v3" stroke="#d0601f" stroke-width="1.3" fill="none"/></svg></div>
    <div class="f-title">Network Solutions</div>
    <p class="f-text">There are many variations of passages of Lorem Ipsum available, but the majority .</p>
    <span class="btn-line">READ MORE</span>
  </div>
  <div class="feature" style="left:408px">
    <div class="f-icon"><svg width="16" height="16" viewBox="0 0 16 16"><path d="M2.5 11V8a5.5 5.5 0 0 1 11 0v3" fill="none" stroke="#d0601f" stroke-width="2"/><rect x="1.5" y="9" width="3.5" height="5" rx="1" fill="#d0601f"/><rect x="11" y="9" width="3.5" height="5" rx="1" fill="#d0601f"/></svg></div>
    <div class="f-title">Onsite Support</div>
    <p class="f-text">The standard chunk of Lorem Ipsum used since the 1500s is reproduced below for.</p>
    <span class="btn-line">READ MORE</span>
  </div>
  <div class="feature" style="left:585px">
    <div class="f-icon"><svg width="17" height="16" viewBox="0 0 17 16" fill="#d0601f"><ellipse cx="7" cy="6" rx="6" ry="4.2"/><path d="M3 9l-1 3 4-2z"/><ellipse cx="11" cy="10" rx="5" ry="3.5" fill="#d0601f" stroke="#fff" stroke-width="1"/></svg></div>
    <div class="f-title">Remote Support</div>
    <p class="f-text">Contrary to popular belief, Lorem Ipsum is not simply random text. It has roots in a piece.</p>
    <span class="btn-line">READ MORE</span>
  </div>
</section>

<section class="services">
  <h2 class="s-heading">OUR SERVCES</h2>
  <div class="s-rule"></div>
  <div class="s-divider"></div>
  <div class="s-icon" style="left:69px;top:106px"><svg width="14" height="14" viewBox="0 0 14 14" fill="#777"><path d="M7 1l6 5.5h-2V13H8.5V9h-3v4H3V6.5H1z"/></svg></div>
  <div class="service" style="left:134px">
    <h3 class="s-title">Home and Residential Services</h3>
    <p class="s-text">There are many variations of passages of Lorem Ipsum available, but the majority have suffered alteration in some form, by injected humour, or randomised words which don't look  even slightly believable.</p>
    <span class="btn-grey">READ MORE</span>
  </div>
  <div class="s-icon" style="left:444px;top:106px"><svg width="16" height="14" viewBox="0 0 16 14" fill="#777"><circle cx="8" cy="4" r="2.5"/><circle cx="3.5" cy="5" r="2"/><circle cx="12.5" cy="5" r="2"/><path d="M4 13a4 4 0 0 1 8 0z"/><path d="M0 11a3.5 3.5 0 0 1 5-3v3z"/><path d="M16 11a3.5 3.5 0 0 0-5-3v3z"/></svg></div>
  <div class="service" style="left:508px">
    <h3 class="s-title">Small business</h3>
    <p class="s-text">Sed ut perspiciatis unde omnis iste natus error sit voluptatem accusantium doloremque laudantium, totam rem aperiam, eaque ipsa quae ab illo inventore veritatis et quasi architecto beatae  vitae dicta sunt explicabo.</p>
    <span class="btn-grey">READ MORE</span>
  </div>
</section>

<footer class="footer">
  <div class="ft-label" style="left:69px">Contact Us</div>
  <div class="ft-label" style="right:67px">Connect With Us</div>
  <p class="ft-contact">PO BOX TBA &nbsp;&nbsp;|&nbsp;&nbsp; T : 0855501234 &nbsp;&nbsp;|&nbsp;&nbsp; E : hello@bramblecrestit.example</p>
  <div class="social"><span class="active"></span><span></span><span></span></div>
  <div class="ft-rule"></div>
  <p class="ft-links">HOME<span>\</span>ABOUT US<span>\</span>SERVICES<span>\</span>BLOG<span>\</span>CONTACT US</p>
  <p class="copyright">Copyrights @ 2015 All Rights Reserved</p>
</footer>
</body>
</html>
```